Holloway Lane Grocer Business Cards
Holloway Lane Grocer
Holloway Lane Grocer Business Cards - Food
Creative Brief
Use specific fonts
Designer choice to compliment font used in logo
Professional
Melissa Carver
Store Manager
274 W Millrace Rd Fort Recovery, OH 45912
melissa@hollowaylanegrocer.example
www.HollowayLaneGrocer.example

```html
<!DOCTYPE html>
<html lang="en">
<head>
<meta charset="utf-8">
<title>Holloway Lane Grocer – Business Card</title>
<link rel="stylesheet" href="https://fonts.googleapis.com/css2?family=Open+Sans:wght@400;600;700&display=swap">
<style>
  :root {
    --backdrop: #2b2b2b;
    --card-white: #ffffff;
    --ink: #111111;
    --ink-soft: #2a2a2a;
    --band: #0d0d0d;
    --on-dark: #ffffff;
    --on-dark-muted: #d6d6d6;
    --divider: #6a6a6a;
  }
  * { box-sizing: border-box; margin: 0; padding: 0; }
  html, body {
    width: 1200px; height: 911px; overflow: hidden;
    background: var(--backdrop);
    font-family: "Open Sans", Arial, sans-serif;
  }
  .stage {
    width: 1200px; height: 911px;
    display: flex; align-items: center; justify-content: center;
  }
  .business-card {
    position: relative;
    width: 1000px; height: 571px;
    background: var(--card-white);
    overflow: hidden;
    box-shadow: 0 18px 40px rgba(0,0,0,.45);
  }
  .crest {
    position: absolute; left: 0; top: 0;
    width: 1000px; height: 300px;
  }
  .brand {
    position: absolute; left: 350px; top: 48px; width: 300px;
    text-align: center; color: var(--on-dark);
  }
  .brand-mark {
    width: 58px; height: 58px; margin: 0 auto 16px;
    border: 3px solid var(--on-dark); border-radius: 50%;
  }
  .brand-name {
    font-weight: 600; font-size: 30px; line-height: 1.15;
    letter-spacing: 2px; text-transform: uppercase;
  }
  .holder {
    position: absolute; left: 0; top: 285px; width: 1000px;
    text-align: center; color: var(--ink);
  }
  .holder-name { font-weight: 700; font-size: 31px; line-height: 1.2; }
  .holder-title { font-weight: 400; font-size: 27px; color: var(--ink-soft); margin-top: 2px; }
  .contact-band {
    position: absolute; left: 0; bottom: 0; width: 1000px; height: 160px;
    background: var(--band); color: var(--on-dark-muted);
    font-size: 17px; line-height: 1.5;
  }
  .contact-item { position: absolute; top: 28px; height: 108px; white-space: nowrap; }
  .contact-item.phone { left: 42px; }
  .contact-item.web { left: 190px; padding-left: 20px; border-left: 1px solid var(--divider); }
  .contact-item.address { left: 570px; padding-left: 20px; border-left: 1px solid var(--divider); }
  .contact-icon { display: block; width: 22px; height: 22px; margin-bottom: 10px; }
  .contact-item strong { color: var(--on-dark); font-weight: 700; }
</style>
</head>
<body>
<main class="stage">
  <article class="business-card">
    <svg class="crest" viewBox="0 0 1000 300" aria-hidden="true">
      <circle cx="500" cy="40" r="218" fill="var(--band)"/>
      <circle cx="500" cy="40" r="204" fill="none" stroke="var(--on-dark)" stroke-width="3"/>
    </svg>

    <div class="brand">
      <div class="brand-mark"></div>
      <p class="brand-name">Holloway Lane Grocer</p>
    </div>

    <div class="holder">
      <h1 class="holder-name">Melissa Carver</h1>
      <p class="holder-title">Store Manager</p>
    </div>

    <footer class="contact-band">
      <div class="contact-item phone">
        <svg class="contact-icon" viewBox="0 0 22 22" aria-hidden="true">
          <rect x="1" y="1" width="20" height="20" rx="3" fill="none" stroke="#fff" stroke-width="1.5"/>
          <path d="M7 6c-1 1-1 3 1 6s4 4 6 4l1.5-1.5-2.5-2-1 1c-1-.5-2-1.5-2.5-2.5l1-1-2-2.5z" fill="#fff"/>
        </svg>
        <p>419-<strong>555</strong>-0142</p>
        <p><strong>419-555-0187</strong></p>
      </div>

      <div class="contact-item web">
        <svg class="contact-icon" viewBox="0 0 22 22" aria-hidden="true">
          <rect x="1" y="1" width="20" height="20" rx="3" fill="none" stroke="#fff" stroke-width="1.5"/>
          <rect x="5.5" y="7" width="11" height="8" fill="none" stroke="#fff" stroke-width="1.4"/>
          <path d="M5.5 7l5.5 4.5L16.5 7" fill="none" stroke="#fff" stroke-width="1.4"/>
        </svg>
        <p>melissa@hollowaylanegrocer.example</p>
        <p>www.HollowayLaneGrocer.<strong>example</strong></p>
      </div>

      <div class="contact-item address">
        <svg class="contact-icon" viewBox="0 0 22 22" aria-hidden="true">
          <rect x="1" y="1" width="20" height="20" rx="3" fill="none" stroke="#fff" stroke-width="1.5"/>
          <path d="M11 17s-4.5-4.6-4.5-7.5a4.5 4.5 0 0 1 9 0C15.5 12.4 11 17 11 17z" fill="#fff"/>
          <circle cx="11" cy="9.5" r="1.6" fill="var(--band)"/>
        </svg>
        <p><strong>274 W</strong> Millrace Rd</p>
        <p>Fort Recovery, OH 45912</p>
      </div>
    </footer>
  </article>
</main>
</body>
</html>
```